Club Flyer

I need a club flyer for an Night Club event I am promoting. The flyer needs to be 2 sided and will be a standard 4.25" x 5.5" club flyer card.

Event Details:
TwistCellar Presents
The Wicked Pixie Bash!!
Saturday November 16th, 2013

Wicked Pixies and Grimwick Ghouls frolicking the night away.

DJ`s:
DJ Brindle Vox
DJR

Featured performers:
Lorna Pike
Dorrie Valcourt
More to be announced.

Featured Photographers to be announced.
H&W Fine Art documenting the entire night on Video.

Costume Contest and Door prizes all night

Target Market(s)

25 to 35 year old club crowd. This is a Gothy, Industrial type club. This is a risque but fun costume event at a night club.

Industry/Entity Type

Club

Requirements
Must have
• Presented by - TwistCellar (Logo Attached)
The Hollowmark (logo Attached) additional files from http://www.hollowmarkvenue.example/
Date - Saturday November 16th, 2013
Time - Doors open at 9pm
Location - The Hollowmark
Address - 4837 Orrin Ave NE. Atlanta, GA
Cost - $10 cover
21+

Imagery of Wicked Pixies and Demons. Should be fun and playful. Think Glimmerwing gone bad and playing with the demons.

```html
<!DOCTYPE html>
<html lang="en">
<head>
<meta charset="utf-8">
<title>The Wicked Pixie Bash – Club Flyer</title>
<link href="https://fonts.googleapis.com/css2?family=Oswald:wght@400;500;700&family=Open+Sans:wght@400;600&display=swap" rel="stylesheet">
<style>
  :root {
    --page: #ffffff;
    --night: #050407;
    --night-glow: #2a2030;
    --gold-light: #fff2a8;
    --gold: #e8b53a;
    --gold-deep: #b07a12;
    --info-grey: #c9c9cf;
    --ice: #c7d3ea;
    --ice-deep: #8e9cc0;
    --title-top: #f4eef8;
    --title-mid: #c9bfd8;
    --title-low: #7d7a92;
    --presenter: #ff2a6a;
    --crystal: #8d8a86;
    --photo-skin: #8a6a66;
    --photo-wing: #5d7ea6;
    --photo-coat: #7a1a22;
    --bucket: #c9ccd2;
  }
  * { margin: 0; padding: 0; box-sizing: border-box; }
  html, body { width: 1200px; height: 828px; overflow: hidden; background: var(--page); }
  .canvas { position: relative; width: 1200px; height: 828px; }

  .flyer {
    position: absolute; top: 18px; width: 540px; height: 780px; overflow: hidden;
    background:
      radial-gradient(ellipse 70% 45% at 50% 42%, var(--night-glow) 0%, transparent 70%),
      var(--night);
  }
  .flyer--front { left: 52px; }
  .flyer--back { left: 618px; }

  .chandelier {
    position: absolute; top: 0; width: 100px; height: 200px;
    background: radial-gradient(ellipse 50% 55% at 50% 45%, var(--crystal) 0%, #3a3836 55%, transparent 80%);
  }
  .chandelier--left { left: 0; }
  .chandelier--right { right: 0; }

  .date {
    position: absolute; top: 48px; left: 0; width: 540px; text-align: center;
    font: 700 28px/1 "Oswald", sans-serif; letter-spacing: 0.5px;
    background: linear-gradient(180deg, var(--gold-light) 0%, var(--gold) 55%, var(--gold-deep) 100%);
    -webkit-background-clip: text; background-clip: text; color: transparent;
  }
  .date-rule {
    position: absolute; top: 84px; left: 130px; width: 280px; height: 1px;
    background: linear-gradient(90deg, transparent, var(--gold), transparent);
  }
  .details {
    position: absolute; top: 96px; left: 0; width: 540px; text-align: center;
    font: 400 12px/1 "Open Sans", sans-serif; color: var(--info-grey); letter-spacing: 0.3px;
  }
  .details .dot { color: var(--gold); margin: 0 4px; }

  .photo { position: absolute; border-radius: 40% 40% 10% 10%; }
  .photo--pixie {
    left: 40px; top: 135px; width: 270px; height: 355px;
    background: radial-gradient(ellipse at 45% 45%, var(--photo-skin) 0%, var(--photo-wing) 45%, transparent 75%);
  }
  .photo--ghoul {
    left: 290px; top: 150px; width: 230px; height: 300px;
    background: radial-gradient(ellipse at 50% 45%, var(--photo-skin) 0%, var(--photo-coat) 45%, #2a2a2e 65%, transparent 80%);
  }

  .djs {
    position: absolute; left: 45px; top: 268px;
    font: 700 22px/1.35 "Oswald", sans-serif; color: var(--ice); text-transform: uppercase;
  }
  .presenter {
    position: absolute; left: 75px; top: 438px;
    font: 700 28px/1 "Oswald", sans-serif; color: var(--presenter); letter-spacing: 1.5px;
  }

  .title {
    position: absolute; left: 0; top: 472px; width: 540px; text-align: center;
    font: 700 94px/0.98 "Oswald", sans-serif; text-transform: uppercase; letter-spacing: 1px;
    background: linear-gradient(180deg, var(--title-top) 0%, var(--title-mid) 35%, var(--title-low) 50%, var(--title-top) 60%, var(--title-mid) 80%, var(--title-low) 100%);
    -webkit-background-clip: text; background-clip: text; color: transparent;
  }

  .entry-rule {
    position: absolute; top: 706px; left: 140px; width: 260px; height: 1px;
    background: linear-gradient(90deg, transparent, #55504a, transparent);
  }
  .entry {
    position: absolute; top: 719px; left: 140px; width: 400px; text-align: center;
    font: 400 11px/1 "Open Sans", sans-serif; color: var(--gold);
  }
  .swirl { position: absolute; left: 0; bottom: 0; }

  .lineup {
    position: absolute; left: 146px; top: 130px;
    font: 700 25px/35px "Oswald", sans-serif; text-transform: uppercase;
    color: var(--ice);
  }
  .lineup .label { color: var(--ice-deep); }
  .notes {
    position: absolute; left: 70px; top: 290px; width: 400px;
    font: 700 16px/1 "Oswald", sans-serif; text-transform: uppercase; color: var(--ice-deep);
  }
  .notes p { margin-bottom: 18px; }
  .photo--bucket {
    left: 375px; top: 255px; width: 130px; height: 190px; border-radius: 20%;
    background: radial-gradient(ellipse at 50% 55%, var(--bucket) 0%, #6a6f7a 45%, transparent 75%);
  }
</style>
</head>
<body>
<main class="canvas">

  <section class="flyer flyer--front" aria-label="Flyer front">
    <div class="chandelier chandelier--left" role="img" aria-label="Crystal chandelier"></div>
    <div class="chandelier chandelier--right" role="img" aria-label="Crystal chandelier"></div>
    <h2 class="date">SAT. NOVEMBER 16TH, 2013</h2>
    <div class="date-rule"></div>
    <p class="details">DRESS CODE<span class="dot">•</span>DOORS 9PM<span class="dot">•</span>21+<span class="dot">•</span>THE HOLLOWMARK</p>

    <div class="photo photo--pixie" role="img" aria-label="Photo of a dancing woman with blue fairy wings"></div>
    <div class="photo photo--ghoul" role="img" aria-label="Photo of a man in a red jacket with horns and dark wings"></div>

    <div class="djs"><p>DJ Brindle Vox</p><p>DJR</p></div>
    <p class="presenter">TwistCellar Presents</p>
    <h1 class="title">The Wicked<br>Pixie Bash!!</h1>

    <div class="entry-rule"></div>
    <p class="entry">$10 COVER • 4837 ORRIN AVE NE, ATLANTA, GA</p>
    <svg class="swirl" width="140" height="80" viewBox="0 0 140 80" aria-hidden="true">
      <path d="M2 80 C 10 30, 80 10, 130 40" fill="none" stroke="#e8e8ee" stroke-width="4" opacity="0.85"/>
      <path d="M14 80 C 22 42, 80 26, 118 50" fill="none" stroke="#ffffff" stroke-width="2" opacity="0.6"/>
    </svg>
  </section>

  <section class="flyer flyer--back" aria-label="Flyer back">
    <div class="chandelier chandelier--left" role="img" aria-label="Crystal chandelier"></div>
    <div class="chandelier chandelier--right" role="img" aria-label="Crystal chandelier"></div>
    <h2 class="date">SAT. NOVEMBER 16TH, 2013</h2>
    <div class="date-rule"></div>
    <p class="details">DRESS CODE<span class="dot">•</span>DOORS 9PM<span class="dot">•</span>21+<span class="dot">•</span>THE HOLLOWMARK</p>

    <div class="lineup">
      <p class="label">Featured Performers:</p>
      <p>Lorna Pike</p>
      <p>Dorrie Valcourt</p>
      <p class="label">More to be announced.</p>
    </div>

    <div class="photo photo--bucket" role="img" aria-label="Champagne bottle in an ice bucket with splashes"></div>

    <div class="notes">
      <p>Featured photographers to be announced.</p>
      <p>H&amp;W Fine Art documenting the entire</p>
      <p>night on video.</p>
      <p>Costume contest and door prizes all night</p>
    </div>

    <h1 class="title">The Wicked<br>Pixie Bash!!</h1>

    <div class="entry-rule"></div>
    <p class="entry">$10 COVER • 4837 ORRIN AVE NE, ATLANTA, GA</p>
    <svg class="swirl" width="140" height="80" viewBox="0 0 140 80" aria-hidden="true">
      <path d="M2 80 C 10 30, 80 10, 130 40" fill="none" stroke="#e8e8ee" stroke-width="4" opacity="0.85"/>
      <path d="M14 80 C 22 42, 80 26, 118 50" fill="none" stroke="#ffffff" stroke-width="2" opacity="0.6"/>
    </svg>
  </section>

</main>
</body>
</html>
```